Veridian Token Bourse (front page)

We need a design of a front page for our Veridian Token Bourse website (vtbex.co.uk). Our company is based in the United Kingdom and offers investors from all over the world an opportunity to invest into bitcoin and litecoin.

We have been developing this cutting edge technology for past 2 years based on our in depth knowledge on conventional stock and currency trading technology and methodology. We have run many test against penetration, security and stability and now are ready to deploy.

Recent news about vulnerability of such platforms leave a great deal of unease from retail investors about investing into cryptocurrency. We are set to challenge this attitude. Our background is payments in particular regulated environment in the UK. We are keen to apply our wealth of experience to provide secure and reliable trading platform and advance cryptocurrency as means of legal tender.

The front page should be based on the feel and look of our current technology vtbex.co.uk. Some of you have already been involved in logo design for our company, please see the attached mockups. The page should have this minimalist design, very clean and light.

Seek inspiration form www.coinharbor.net, www.tradelumo.com, vip.quorzen.com and other bitcoin exchanges.

We look forward to receiving your ideas.

You can also refer to our social pages:
https://www.facebook.com/vtbex.co.uk
https://twitter.com/vtbex_uk

We would like you to focus your efforts at designing the page in such a way so that it is very easy for visitor be open an account with the exchange. We must focus at informing the visitor about the bitcoin, how to my buy, how to sell, look at the general overview of the maker and CONVERTING him/her sing up. This is the most important!!

Regards,
Tobin
Updates

Project Deadline Extended
Reason: Dear all, We are very keen on getting this design done right the first time. The key success is conversion of visitors to subscribers and then to traders. It is absolutely essential make the registration process as streamlined as possible! When we are calling them to act by "Change the world one bitcoin at a time" we should give them a opportunity to provide us with relevant account creation details: email, password, confirm password. Please visit remitfold.co.uk for ideas. Secondly, tell them what is a bitcoin, why a bitcoin is a good investment and how to invest. Finally, it is important to inform visitors of "who we are", what sets us apart from other exchanges, tell them about our experience. In our view graphs and live order books are important but they might turn some visitors away especially the ones that are not accustomed to online trading. Think of what would you like to see on the page if you wanted YOURSELF to invest. What would make you to create an account and use it? Think what will work, we are here to revolutionise how people do business.... any wild ideas put them to us. OUR BUDGET JUST GONE UP!!!

Target Market(s)

A combination of professional and consumer bitcoin investors.

Industry/Entity Type

Environment

Requirements
Must have
• News section

```html
<!DOCTYPE html>
<html lang="en">
<head>
<meta charset="utf-8">
<title>Veridian Token Bourse</title>
<link href="https://fonts.googleapis.com/css2?family=Open+Sans:wght@400;600;700&family=Raleway:wght@300;400;600&display=swap" rel="stylesheet">
<style>
:root{
  --bar:#2c2c2c;
  --bar-text:#8a8a8a;
  --bar-value:#4fb7e8;
  --header:#f4f4f4;
  --sky:#6ec6ea;
  --sky-dark:#4fb2de;
  --orange:#f9a94a;
  --orange-text:#f7941d;
  --ink:#4a4a4a;
  --muted:#8c8c8c;
  --slate:#8fb0c2;
  --panel:#f4f4f4;
  --line:#dcdcdc;
  --sell-row:#fdefd2;
  --ask:#e4f8fb;
  --bid:#fdecd8;
  --price-col:#eef8fb;
  --white:#ffffff;
  --footer:#77c8ee;
}
*{box-sizing:border-box;margin:0;padding:0}
html,body{width:1200px;height:2571px;overflow:hidden}
body{font-family:"Open Sans",Arial,sans-serif;color:var(--ink);background:var(--white);position:relative}

.topbar{position:absolute;top:0;left:0;width:1200px;height:53px;background:var(--bar)}
.ticker{position:absolute;top:9px;font-size:11px;color:var(--bar-text);line-height:1.2}
.ticker b{display:block;font-weight:400;font-size:16px;color:var(--bar-value)}
.ticker-sep{position:absolute;top:0;width:1px;height:53px;background:#3d3d3d}
.lang{position:absolute;left:785px;top:9px;width:82px;height:36px;background:#505050;color:#eee;font-size:13px;padding:9px 10px;border-radius:2px}
.lang:after{content:"";position:absolute;right:10px;top:16px;border:5px solid transparent;border-top-color:#eee}
.bar-btn{position:absolute;top:9px;height:36px;font-size:12px;font-weight:700;color:#fff;text-align:center;line-height:36px;border-radius:2px}
.signup{left:878px;width:68px;background:var(--orange)}
.login{left:955px;width:68px;background:var(--sky)}

.header{position:absolute;top:53px;left:0;width:1200px;height:125px;background:var(--header)}
.brand{position:absolute;left:177px;top:48px;font-size:20px;font-weight:600;color:#333;line-height:28px;white-space:nowrap}
.nav{position:absolute;top:45px;left:494px;display:flex}
.nav a{font-size:15px;color:#555;text-decoration:none;height:36px;line-height:36px;padding:0 12px;margin-right:21px}
.nav a.active{background:var(--sky);color:#fff;border-radius:2px}

.hero{position:absolute;top:178px;left:0;width:1200px;height:367px;background:var(--sky)}
.hero-map{position:absolute;inset:0;background:radial-gradient(ellipse at 50% 40%,#82d0ef 0%,var(--sky) 70%)}
.hero-icons{position:absolute;top:40px;left:393px}
.rate{position:absolute;top:204px;width:1200px;text-align:center;color:#fff;font-size:22px;font-weight:600}
.cta{position:absolute;left:447px;top:264px;width:307px;height:67px;background:var(--orange);border:2px solid #fff3;border-radius:4px;color:#fff;font-family:"Raleway",sans-serif;font-size:24px;font-weight:600;text-align:center;line-height:63px;box-shadow:0 2px 0 #e08d2c}

.tagline{position:absolute;left:291px;top:557px;width:600px;height:86px;background:linear-gradient(#fff,#f3f3f3 50%,#fff)}

.features{position:absolute;top:660px;left:0;width:1200px}
.feature{position:absolute;width:240px;text-align:center;font-size:15px;line-height:24px;color:var(--muted)}
.feature-icon{width:92px;height:92px;border-radius:50%;margin:2px auto 0;display:flex;align-items:center;justify-content:center}
.feature h2{font-family:"Raleway",sans-serif;font-weight:400;font-size:25px;color:#444;margin:10px 0 9px}
.date{color:#3aabe0}
.headline{color:var(--orange-text);font-weight:600}
.more{display:inline-block;margin-top:18px;width:124px;height:38px;background:var(--slate);color:#fff;font-size:11px;font-weight:700;line-height:38px;border-radius:2px}
.more:after{content:"";display:inline-block;margin-left:10px;border:4px solid transparent;border-left-color:#fff}

.market{position:absolute;top:1063px;left:0;width:1200px;height:905px;background:var(--panel);border-top:1px solid var(--line);border-bottom:1px solid var(--line)}
.section-title{position:absolute;left:190px;font-family:"Raleway",sans-serif;font-weight:400;font-size:30px;color:#3aabe0}
.ranges{position:absolute;left:198px;top:113px;display:flex;gap:3px}
.ranges span{font-size:10px;color:#888;background:#ececec;border:1px solid #ddd;padding:1px 4px}
.pair{position:absolute;left:190px;top:110px;width:815px;text-align:center;font-size:14px;font-weight:600;color:#555}
.chart{position:absolute;left:190px;top:132px;width:815px;height:281px;background:#fff;border:1px solid var(--line)}
.chart-tabs{position:absolute;left:0;bottom:0;width:100%;height:22px;display:flex}
.chart-tabs span{flex:1;text-align:center;font-size:11px;color:#999;border:1px solid var(--line);line-height:20px}
.chart-tabs span.on{color:#555;border-color:transparent}

.trades{position:absolute;left:190px;top:473px;width:815px;border-collapse:collapse;background:#fff;font-size:12px;color:#666}
.trades th{height:43px;background:#ececec;text-align:left;font-weight:600;color:#555;font-size:13px;padding-left:10px;border-bottom:1px solid var(--line)}
.trades td{height:34px;padding-left:10px;border-bottom:1px solid #eee}
.trades tr.sell td{background:var(--sell-row)}

.trade-panel{position:absolute;top:1968px;left:0;width:1200px;height:521px}
.tabs{position:absolute;left:190px;top:46px;display:flex}
.tab{width:125px;height:51px;text-align:center;font-size:13px;padding-top:6px;line-height:17px;color:#555}
.tab b{font-weight:400;font-size:14px;display:block}
.tab.buy{background:#fff;border:1px solid #dde;border-bottom:none}
.tab.buy b{color:var(--orange-text)}
.tab.sell{background:#dde9ee}
.tab.sell b{color:#3aabe0}
.order-form{position:absolute;left:190px;top:97px;width:401px;height:355px;background:#f7fcfe;border:1px solid #dbe8ee}
.field{position:absolute;left:22px;font-size:14px;color:#666}
.input{position:absolute;left:139px;width:238px;height:41px;background:#e6f3f8;border:1px solid #c9dde6;border-radius:2px;font-size:14px;padding:10px 14px;color:#555}
.input.select:after{content:"";position:absolute;right:14px;top:17px;border:6px solid transparent;border-top-color:#4fb2de}
.summary{position:absolute;left:12px;top:184px;width:377px;height:86px;background:#e3f4fb;border:1px solid #cfe6ef;font-size:13px}
.summary div{height:43px;line-height:43px;padding-left:12px;border-bottom:1px solid #cfe6ef}
.summary b{position:absolute;left:130px;color:#333}
.form-btn{position:absolute;top:287px;width:168px;height:51px;color:#fff;font-size:13px;font-weight:700;text-align:center;line-height:51px;border-radius:2px}
.form-btn.go{left:22px;background:var(--orange)}
.form-btn.stop{left:206px;background:var(--slate)}
.bid-title{position:absolute;left:610px;top:52px;font-family:"Raleway",sans-serif;font-weight:400;font-size:25px;color:var(--orange)}
.book{position:absolute;left:608px;top:97px;width:397px;border-collapse:collapse;font-size:12px;color:#555}
.book th{height:43px;text-align:left;padding-left:20px;font-size:12px;color:#3a7da0;font-weight:600;border:1px solid #d4eaf2;background:#fff}
.book td{height:34px;padding-left:20px;border:1px solid #fff;width:33%}
.book td.price{background:var(--price-col)}
.book tr.ask td.side{background:var(--ask)}
.book tr.ask td.empty{background:#f1fafc}
.book tr.bid td.side{background:var(--bid)}
.book tr.bid td.price{background:#fdf2e4}
.book tr.bid td.empty{background:#f1fafc}

.footer{position:absolute;top:2489px;left:0;width:1200px;height:82px;background:var(--footer);text-align:center}
.footer-nav{padding-top:13px;font-size:13px;color:#1e3a4a}
.footer-nav span{margin:0 14px}
.copy{margin-top:9px;font-size:11px;color:#eef}
</style>
</head>
<body>

<div class="topbar">
  <div class="ticker" style="left:177px">Last price<b>13.72 EUR</b></div>
  <div class="ticker-sep" style="left:300px"></div>
  <div class="ticker" style="left:315px">Low price<b>11.4 EUR</b></div>
  <div class="ticker-sep" style="left:424px"></div>
  <div class="ticker" style="left:439px">High price<b>12.4 EUR</b></div>
  <div class="ticker-sep" style="left:547px"></div>
  <div class="ticker" style="left:562px">Volum<b>197.4 LTC</b></div>
  <div class="ticker-sep" style="left:678px"></div>
  <div class="lang">English</div>
  <div class="bar-btn signup">SIGN UP</div>
  <div class="bar-btn login">LOGIN</div>
</div>

<header class="header">
  <div class="brand">Veridian Token Bourse</div>
  <nav class="nav">
    <a class="active">Home</a><a>Features</a><a>API Trade</a><a>Account</a><a>Contacts</a><a>Support</a>
  </nav>
</header>

<section class="hero">
  <div class="hero-map" role="img" aria-label="Dotted world map with a rising price line across the background"></div>
  <svg class="hero-icons" width="414" height="134" viewBox="0 0 414 134">
    <circle cx="65" cy="65" r="65" fill="#fff"/>
    <circle cx="65" cy="65" r="36" fill="#4fb2de"/>
    <path d="M65 42 V65 H84" stroke="#fff" stroke-width="7" fill="none" stroke-linecap="round"/>
    <circle cx="207" cy="65" r="65" fill="#fff"/>
    <circle cx="207" cy="65" r="40" fill="#4fb2de"/>
    <ellipse cx="207" cy="65" rx="18" ry="40" fill="none" stroke="#fff" stroke-width="4"/>
    <path d="M167 65 H247 M173 45 H241 M173 85 H241" stroke="#fff" stroke-width="4"/>
    <circle cx="348" cy="65" r="65" fill="#fff"/>
    <path d="M348 106 C330 82 322 70 322 56 A26 26 0 0 1 374 56 C374 70 366 82 348 106Z" fill="#4fb2de"/>
    <circle cx="348" cy="56" r="10" fill="#fff"/>
  </svg>
  <div class="rate">Sell BTC 604.29200 USD &nbsp;|&nbsp; Buy BTC 605.49800 USD</div>
  <div class="cta">Open your FREE Account</div>
</section>

<div class="tagline" role="img" aria-label="Hand-lettered slogan: Change the world one bitcoin at a time"></div>

<section class="features">
  <div class="feature" style="left:180px">
    <div class="feature-icon" style="background:#f7941d">
      <svg width="44" height="36" viewBox="0 0 44 36"><g fill="#fff"><rect x="0" y="2" width="6" height="6"/><rect x="10" y="2" width="34" height="6"/><rect x="0" y="15" width="6" height="6"/><rect x="10" y="15" width="34" height="6"/><rect x="0" y="28" width="6" height="6"/><rect x="10" y="28" width="34" height="6"/></g></svg>
    </div>
    <h2>Overview</h2>
    <p>Lorem ipsum dolor sit amet, consectetur adipiscing elit. Sed quis nisi euismod, fermentum tellus a, lobortis quam. Vestibulum condimentum mi vitae diam tristique.</p>
    <span class="more">KNOW MORE</span>
  </div>
  <div class="feature" style="left:478px">
    <div class="feature-icon" style="background:#4fb2de">
      <svg width="60" height="20" viewBox="0 0 60 20"><g fill="#fff"><circle cx="9" cy="10" r="8"/><circle cx="30" cy="10" r="8"/><circle cx="51" cy="10" r="8"/></g></svg>
    </div>
    <h2>Who We Are</h2>
    <p>Lorem ipsum dolor sit amet, consectetur adipiscing elit. Sed quis nisi euismod, fermentum tellus a, lobortis quam. Vestibulum condimentum mi vitae diam tristique.</p>
    <span class="more">KNOW MORE</span>
  </div>
  <div class="feature" style="left:777px">
    <div class="feature-icon" style="background:#6cbf3c">
      <svg width="40" height="40" viewBox="0 0 40 40"><rect x="2" y="2" width="36" height="36" fill="none" stroke="#fff" stroke-width="4"/><g fill="#fff"><rect x="10" y="22" width="5" height="10"/><rect x="18" y="14" width="5" height="18"/><rect x="26" y="9" width="5" height="23"/></g></svg>
    </div>
    <h2>News</h2>
    <p><span class="date">21st March 2014</span><br><span class="headline">Consectetur adipiscing elit.</span><br>Sed quis nisi euismod, fermentum tellus a, lobortis quam. Vestibulum condimentum mi vitae diam tristique........</p>
    <span class="more">KNOW MORE</span>
  </div>
</section>

<section class="market">
  <h2 class="section-title" style="top:52px">Graph Overview</h2>
  <div class="ranges"><span>M1</span><span>M5</span><span>M15</span><span>M30</span><span>H1</span><span>H4</span></div>
  <div class="pair">LTC/EUR</div>
  <div class="chart">
    <svg width="815" height="259" viewBox="0 0 815 259">
      <defs><linearGradient id="fill" x1="0" y1="0" x2="0" y2="1"><stop offset="0" stop-color="#bfe3f5"/><stop offset="1" stop-color="#eef8fd"/></linearGradient></defs>
      <g stroke="#f0f0f0"><line x1="45" y1="53" x2="815" y2="53"/><line x1="45" y1="110" x2="815" y2="110"/><line x1="45" y1="151" x2="815" y2="151"/></g>
      <path d="M45 41 H473 L495 82 L576 151 H718 L770 190 H809 V207 H45Z" fill="url(#fill)"/>
      <path d="M45 41 H473 L495 82 L576 151 H718 L770 190 H809" fill="none" stroke="#6ab8df" stroke-width="2"/>
      <line x1="473" y1="30" x2="473" y2="207" stroke="#a8d5ec"/>
      <line x1="45" y1="207" x2="815" y2="207" stroke="#ddd"/>
      <g font-size="11" fill="#666" font-family="Open Sans,sans-serif">
        <text x="6" y="57">12.2000</text><text x="6" y="114">11.8</text><text x="6" y="155">11.5</text>
        <text x="110" y="222">15:45</text><text x="238" y="222">15:55</text><text x="368" y="222">16:05</text><text x="497" y="222">16:15</text><text x="625" y="222">16:25</text>
      </g>
      <rect x="389" y="34" width="84" height="43" rx="3" fill="#fff" stroke="#ccc"/>
      <circle cx="400" cy="46" r="4" fill="none" stroke="#555"/>
      <text x="408" y="50" font-size="10" fill="#444" font-family="Open Sans,sans-serif">4:13:00 PM</text>
      <text x="397" y="70" font-size="11" fill="#444" font-family="Open Sans,sans-serif">12.0500</text>
      <circle cx="473" cy="77" r="3" fill="#fff" stroke="#6ab8df"/>
    </svg>
    <div class="chart-tabs"><span class="on">QUOTES</span><span>CANDLES</span><span>VOLUME</span></div>
  </div>

  <table class="trades">
    <tr><th>Market</th><th>Time</th><th>Type</th><th>Volume (LTC)</th><th>Price</th><th>Total (EUR)</th></tr>
    <tr><td>LTC/EUR</td><td>3/18/2014 10:54:50 PM</td><td>Buy</td><td>6.87191</td><td>13.72</td><td>94.2826</td></tr>
    <tr><td>LTC/EUR</td><td>3/18/2014 10:50:04 PM</td><td>Buy</td><td>0.11408</td><td>13.624</td><td>1.5542</td></tr>
    <tr><td>LTC/EUR</td><td>3/18/2014 10:43:48 PM</td><td>Buy</td><td>7.54633</td><td>13.549</td><td>102.2452</td></tr>
    <tr><td>LTC/EUR</td><td>3/18/2014 10:36:13 PM</td><td>Buy</td><td>5.34759</td><td>13.598</td><td>72.7165</td></tr>
    <tr class="sell"><td>LTC/EUR</td><td>3/18/2014 10:23:35 PM</td><td>Sell</td><td>1.82485</td><td>13.507</td><td>24.6482</td></tr>
    <tr><td>LTC/EUR</td><td>3/18/2014 10:54:50 PM</td><td>Buy</td><td>6.87191</td><td>13.72</td><td>94.2826</td></tr>
    <tr><td>LTC/EUR</td><td>3/18/2014 10:50:04 PM</td><td>Buy</td><td>0.11408</td><td>13.624</td><td>1.5542</td></tr>
    <tr><td>LTC/EUR</td><td>3/18/2014 10:43:48 PM</td><td>Buy</td><td>7.54633</td><td>13.549</td><td>102.2452</td></tr>
    <tr><td>LTC/EUR</td><td>3/18/2014 10:36:13 PM</td><td>Buy</td><td>5.34759</td><td>13.598</td><td>72.7165</td></tr>
    <tr class="sell"><td>LTC/EUR</td><td>3/18/2014 10:23:35 PM</td><td>Sell</td><td>1.82485</td><td>13.507</td><td>24.6482</td></tr>
  </table>
</section>

<section class="trade-panel">
  <div class="tabs">
    <div class="tab buy"><b>Buy LTC</b>11.50200 EUR</div>
    <div class="tab sell"><b>Sell LTC</b>11.38100 EUR</div>
  </div>
  <div class="order-form">
    <span class="field" style="top:28px">Type</span>
    <div class="input select" style="top:17px">Limit</div>
    <span class="field" style="top:81px">Volume LTC</span>
    <div class="input" style="top:70px"></div>
    <span class="field" style="top:133px">Price per LTC</span>
    <div class="input" style="top:122px"></div>
    <div class="summary">
      <div>Total :<b>EUR 0.00</b></div>
      <div style="border:none">Fee :<b>EUR 0.00</b></div>
    </div>
    <div class="form-btn go">SELL LTC</div>
    <div class="form-btn stop">CANCEL</div>
  </div>

  <h2 class="bid-title">Bidding</h2>
  <table class="book">
    <tr><th>BID</th><th>PRICE</th><th>ASK</th></tr>
    <tr class="ask"><td class="empty"></td><td class="price">11.87000</td><td class="side">5.79603</td></tr>
    <tr class="ask"><td class="empty"></td><td class="price">11.86900</td><td class="side">0.29862</td></tr>
    <tr class="ask"><td class="empty"></td><td class="price">11.81100</td><td class="side">3.70862</td></tr>
    <tr class="ask"><td class="empty"></td><td class="price">11.80800</td><td class="side">56.10440</td></tr>
    <tr class="ask"><td class="empty"></td><td class="price">11.80400</td><td class="side">0.24006</td></tr>
    <tr class="bid"><td class="side">1.35484</td><td class="price">11.61100</td><td class="empty"></td></tr>
    <tr class="bid"><td class="side">0.23305</td><td class="price">11.57100</td><td class="empty"></td></tr>
    <tr class="bid"><td class="side">0.78467</td><td class="price">11.55000</td><td class="empty"></td></tr>
    <tr class="bid"><td class="side">1.35484</td><td class="price">11.61100</td><td class="empty"></td></tr>
  </table>
</section>

<footer class="footer">
  <div class="footer-nav"><span>Home</span><span>Features</span><span>API Trade</span><span>Account</span><span>Contacts</span><span>Support</span></div>
  <div class="copy">© 2014 Veridian Token Bourse Limited. All rights reserved</div>
</footer>

</body>
</html>
```